Homepage Design :) --- A website that connects Journalists to Sources to make brilliant news stories

I need a new homepage designed for a company based in California. The homepage is simple.
The website is QuillBridgeConnect.com.

About us:
We are a platform that connects reporters to expert sources (normal people with specific expertise) so a reporter can quickly and easily source information for their news story. Also, the source gets cited in their major news article so it's a win-win situation.

Design:
We have no real slogan except maybe the slogan on the website (beautiful stories that connect us), though that can change too.

I would like to see designs of any style that you choose. We really only have one website color shown in blue on the website, you can use other colors in addition to that one or even change the theme color.

Attachments:
- Homepage to redesign, which you can go to the website yourself to check it out
- A mockup sketch of a revision idea that I had in mind with two people thinking short thoughts. Though this is just a random thought.... You can make anything you want! :)
- An image of what the logged in dashboard looks like just if you want a reference

The footer menu links will remain but can be anything color/style.

Make any ideas you want, keep the same amount of sections or add more, add any graphics or things that you want, etc. I want creativity to really attract customers the second they land on the page. A powerfully beautiful home page!

For reference, some competing websites are NewsDeskLink.com, Vornip.io, and plivex.com
I noticed all these website use red/orange related colors, so maybe I should change the color theme to that? Again, your decision :)

```html
<!DOCTYPE html>
<html lang="en">
<head>
<meta charset="utf-8">
<title>QuillBridge Connect — Beautiful Stories That Connect Us</title>
<link href="https://fonts.googleapis.com/css2?family=Roboto+Slab:wght@300;400;700&family=Open+Sans:wght@400;600&display=swap" rel="stylesheet">
<style>
:root{
  --orange:#f26a2b;
  --ink:#2f3a43;
  --slate:#4b5862;
  --slate-dark:#2d3942;
  --paper:#ffffff;
  --mist:#eef0f2;
  --muted:#8a949b;
  --light:#e6e9eb;
}
*{margin:0;padding:0;box-sizing:border-box}
html,body{width:702px;height:1200px;overflow:hidden;background:var(--paper)}
body{font-family:"Open Sans",Arial,sans-serif;color:var(--ink)}
.page{position:relative;width:702px;height:1200px;overflow:hidden}
.serif{font-family:"Roboto Slab",Georgia,serif}

/* header */
.site-header{position:absolute;top:0;left:0;right:0;height:44px}
.brand{position:absolute;left:33px;top:10px;font-family:"Roboto Slab",Georgia,serif;font-weight:700;font-size:22px;color:var(--ink);line-height:1}
.brand small{display:block;font-size:5.5px;letter-spacing:.8px;margin-top:3px;font-weight:700}
.nav{position:absolute;right:78px;top:14px;display:flex;gap:10px;align-items:center;font-size:9px}
.nav a{color:var(--ink);text-decoration:none}
.btn-sm{display:inline-block;padding:4px 12px;border-radius:3px;color:#fff !important;font-size:8.5px}
.btn-orange{background:var(--orange)}
.btn-dark{background:var(--slate-dark)}

/* hero */
.hero-eyebrow{position:absolute;top:56px;width:100%;text-align:center;font-size:10px;letter-spacing:.6px;color:var(--orange);font-weight:600}
.hero-title{position:absolute;top:70px;width:100%;text-align:center;font-weight:300;font-size:30px;color:var(--ink)}
.hero-art{position:absolute;left:170px;top:118px;width:350px;height:262px;border-radius:8px;background:radial-gradient(ellipse at 50% 60%,#e9ecee 0%,#f6f7f8 55%,#fff 80%)}
.bubble{position:absolute;font-family:"Roboto Slab",Georgia,serif;font-size:13px;line-height:1.25}
.bubble-reporter{left:74px;top:168px;width:112px;height:88px;border-radius:44px;background:var(--slate-dark);color:#fff;padding:14px 10px 0 16px}
.bubble-reporter b{font-weight:700}
.bubble-source{left:505px;top:142px;width:140px;color:var(--orange);font-size:14px}
.bubble-source b{font-weight:700}
.pill{position:absolute;display:flex;align-items:center;gap:6px;background:var(--orange);color:#fff;font-size:9px;padding:5px 11px;border-radius:12px}
.pill svg{width:7px;height:7px}

/* mission band */
.mission{position:absolute;top:385px;left:0;width:702px;height:126px;background:var(--slate);color:#eef1f3;text-align:center;padding-top:27px;font-family:"Roboto Slab",Georgia,serif;font-weight:300;font-size:17px;line-height:1.42}
.mission u{text-decoration-color:var(--orange);text-underline-offset:4px}

/* how it works */
.how{position:absolute;top:511px;left:0;width:702px;height:295px;background:var(--paper)}
.how h2{position:absolute;left:33px;top:34px;font-family:"Roboto Slab",Georgia,serif;font-weight:300;font-size:26px}
.how h2::after{content:"";display:block;width:170px;height:1px;background:var(--light);margin-top:6px}
.step{position:absolute;left:33px;width:280px;display:flex;gap:18px}
.step .num{font-family:"Roboto Slab",Georgia,serif;font-weight:300;font-size:26px;width:28px;color:var(--ink)}
.step h3{font-family:"Roboto Slab",Georgia,serif;font-weight:400;font-size:12px;margin-top:6px}
.step p{font-size:6.5px;color:var(--muted);margin-top:4px;line-height:1.5;width:190px}
.how-art{position:absolute;left:372px;top:30px;width:290px;height:250px;border-radius:50%;background:radial-gradient(circle at 50% 50%,#fde3d6 0%,#fdf1ea 45%,#fff 72%)}

/* audiences */
.audiences{position:absolute;top:806px;left:0;width:702px;height:200px;display:flex}
.aud{flex:1;padding:26px 0 0 33px;color:#fff}
.aud-reporters{background:var(--orange)}
.aud-sources{background:var(--slate-dark);padding-left:28px}
.aud h2{font-family:"Roboto Slab",Georgia,serif;font-weight:300;font-size:22px}
.aud h2::after{content:"";display:block;width:160px;height:1px;background:rgba(255,255,255,.35);margin-top:6px}
.aud ul{list-style:none;margin-top:12px;font-size:8.5px;line-height:1.35}
.aud li{position:relative;padding-left:16px;margin-bottom:8px;width:270px}
.aud li::before{content:"";position:absolute;left:0;top:4px;width:4px;height:4px;border-radius:50%;background:#fff}
.aud .btn-sm{margin-top:4px;padding:6px 12px;font-size:8.5px}

/* footer */
.site-footer{position:absolute;top:1006px;left:0;width:702px;height:194px;background:var(--slate);color:#d7dde1}
.site-footer .brand{top:28px;left:33px;color:#fff;font-size:30px}
.site-footer .brand small{font-size:7px}
.fcol{position:absolute;top:34px;font-size:7px;line-height:1.7}
.fcol h4{font-size:7.5px;font-weight:600;letter-spacing:.5px;color:#fff;margin-bottom:3px}
.fcol h4::after{content:"";display:block;width:14px;height:1px;background:var(--orange);margin-top:2px}
.copyright{position:absolute;bottom:12px;width:100%;text-align:center;font-size:6.5px;color:#c2c9ce;border-top:1px solid rgba(255,255,255,.15);padding-top:10px;left:0}
</style>
</head>
<body>
<div class="page">

  <header class="site-header">
    <div class="brand">QBC<small>QUILLBRIDGE CONNECT</small></div>
    <nav class="nav">
      <a href="#how">How It Works</a>
      <a class="btn-sm btn-orange" href="#signup">Sign Up</a>
      <a class="btn-sm btn-dark" href="#login">Login</a>
    </nav>
  </header>

  <section class="hero">
    <p class="hero-eyebrow">EXPERIENCE INSPIRING REPORTING</p>
    <h1 class="hero-title serif">Beautiful Stories &nbsp;That Connect Us</h1>
    <div class="hero-art" role="img" aria-label="Illustration of a reporter holding a microphone interviewing an expert source, with trees in the background"></div>
    <div class="bubble bubble-reporter"><b>I'm a reporter.</b> I want to find expert sources for my articles.</div>
    <a class="pill" style="left:77px;top:290px">Reporters <svg viewBox="0 0 8 8"><path d="M2 1l3 3-3 3" stroke="#fff" stroke-width="1.4" fill="none"/></svg></a>
    <div class="bubble bubble-source"><b>I'm an expert source.</b> I can simply provide my knowledge and get cited.</div>
    <a class="pill" style="left:568px;top:283px">Sources <svg viewBox="0 0 8 8"><path d="M2 1l3 3-3 3" stroke="#fff" stroke-width="1.4" fill="none"/></svg></a>
  </section>

  <section class="mission">
    <p><u>QuillBridge Connect (QBC)</u> connects<br>reporters and sources from around the world.<br>You want real, honest stories. We connect you to the experts.</p>
  </section>

  <section class="how" id="how">
    <h2>How It Works</h2>
    <div class="step" style="top:98px"><span class="num">01</span><div><h3>Post a query</h3><p>Looking for information on a story, etc</p></div></div>
    <div class="step" style="top:175px"><span class="num">02</span><div><h3>Respond to a Query</h3><p>Looking to add value to an article or news, etc</p></div></div>
    <div class="step" style="top:230px"><span class="num">03</span><div><h3>Let the magic happen</h3><p>With great information comes great stories. The beauty of this community is that with the collaboration you produce the best form of media and information.</p></div></div>
    <div class="how-art" role="img" aria-label="Illustration of a person working with floating screens and charts"></div>
  </section>

  <section class="audiences">
    <div class="aud aud-reporters">
      <h2>Reporters</h2>
      <ul>
        <li>Find sources for the stories that you need information</li>
        <li>Browse profiles of your sources to verify expertise</li>
        <li>Explore stories to discover new topics</li>
      </ul>
      <a class="btn-sm btn-dark" href="#reporter-signup">Reporters Signup</a>
    </div>
    <div class="aud aud-sources">
      <h2>Sources</h2>
      <ul>
        <li>Connect your expertise with reporters to be sourced in their articles</li>
        <li>Browse recommended reporter queries based on your categories of interest/expertise</li>
        <li>Pitch new story ideas to reporters, at whatever price you decide</li>
      </ul>
      <a class="btn-sm btn-orange" href="#source-signup">Source Signup</a>
    </div>
  </section>

  <footer class="site-footer">
    <div class="brand">QBC<small>QUILLBRIDGE CONNECT</small></div>
    <div class="fcol" style="left:276px"><h4>ABOUT</h4>Contact us<br>How it works<br>Job board / hiring board</div>
    <div class="fcol" style="left:402px"><h4>INFORMATION</h4>Terms of Service<br>Privacy Policy</div>
    <div class="fcol" style="left:510px"><h4>RULES</h4>Reporter &amp; Source Rules<br>Refund Policy</div>
    <p class="copyright">Copyright © 2022. All Rights Reserved.</p>
  </footer>

</div>
</body>
</html>
```